Business Card for Auto Dealership - Clean, sharp and professional

Please use the maroon logo with the grey background. Need a sharp, clean and professional business card for an Auto Dealer. In the files provides there is three different logos. I have not decided which one to go with yet. Right now I am favoring the grey/silver background. I would like my contact info on there and the website as well. I feel like less is more and want something simple, clean and sharp. Thank you in advance for your tie and effort! I also need email signature, letterhead, etc after this

Target Market(s)

Car buyers

Industry/Entity Type

Automotive

Contact Information for Business Card

Drew
555-214-7730
www.BriarvaleAutoLink.example
Drew@BriarvaleAutoLink.example

Font styles to use
Serif
Sans Serif

Requirements
Must have
• Please use the maroon logo with the grey background. Business Card Details and logo from files. Please stick to the logo colors

```html
<!DOCTYPE html>
<html lang="en">
<head>
<meta charset="utf-8">
<title>Briarvale Auto Link – Business Card</title>
<link rel="stylesheet" href="https://fonts.googleapis.com/css2?family=Saira:wght@700&family=Roboto:wght@400;500;700&display=swap">
<style>
  :root {
    --maroon: #4a1c1f;
    --maroon-deep: #3a1518;
    --card-light: #cdcdcd;
    --card-dark: #b2b2b2;
    --ribbon: #d6d6d6;
    --backdrop: #ececec;
    --white: #ffffff;
  }
  * { margin: 0; padding: 0; box-sizing: border-box; }
  html, body { width: 1200px; height: 576px; overflow: hidden; background: var(--backdrop); }
  .stage { position: relative; width: 1200px; height: 576px; }
  .card {
    position: absolute;
    width: 482px; height: 292px;
    border-radius: 10px;
    overflow: hidden;
    background: linear-gradient(180deg, var(--card-light) 0%, var(--card-dark) 100%);
  }
  .card--front { left: 82px; top: 139px; }
  .card--back  { left: 602px; top: 138px; }

  .brand { position: absolute; display: flex; align-items: center; gap: 14px; }
  .brand__dot {
    width: 68px; height: 68px; border-radius: 50%;
    background: var(--maroon); flex: none;
  }
  .brand__name {
    font-family: "Saira", sans-serif; font-weight: 700;
    color: var(--maroon); line-height: 1;
  }
  .brand__main { display: block; font-size: 26px; letter-spacing: 1.5px; }
  .brand__sub  { display: block; font-size: 9.5px; letter-spacing: 5.4px; margin-top: 3px; }
  .card--front .brand { left: 116px; top: 112px; }
  .card--back .brand  { left: 20px; top: 36px; }

  .wave { position: absolute; left: 0; top: 0; width: 482px; height: 292px; }

  .contact {
    position: absolute; left: 38px; top: 154px;
    list-style: none;
    font-family: "Roboto", sans-serif; font-size: 11.5px; color: var(--maroon-deep);
  }
  .contact li { display: flex; align-items: center; gap: 9px; height: 16.5px; }
  .contact svg { width: 10px; height: 10px; fill: var(--maroon-deep); flex: none; }

  .person {
    position: absolute; right: 34px; top: 222px; text-align: right;
    font-family: "Roboto", sans-serif; color: var(--white);
  }
  .person__name { font-size: 19px; font-weight: 700; letter-spacing: 0.5px; line-height: 1; }
  .person__role { font-size: 10.5px; margin-top: 5px; }
</style>
</head>
<body>
<main class="stage">
  <section class="card card--front" aria-label="Card front">
    <div class="brand">
      <span class="brand__dot"></span>
      <span class="brand__name">
        <span class="brand__main">BRIARVALE</span>
        <span class="brand__sub">AUTO LINK</span>
      </span>
    </div>
  </section>

  <section class="card card--back" aria-label="Card back">
    <svg class="wave" viewBox="0 0 482 292" aria-hidden="true">
      <path fill="var(--maroon-deep)" d="M0,232 C110,262 220,258 290,212 C350,172 410,150 482,144 L482,292 L0,292 Z"/>
      <path fill="var(--ribbon)" opacity="0.85" d="M0,250 C120,278 230,268 300,226 C360,188 420,166 482,160 L482,166 C420,174 362,198 304,236 C232,282 118,288 0,262 Z"/>
      <path fill="var(--ribbon)" opacity="0.7" d="M40,236 C150,250 240,236 310,196 C240,246 150,262 40,240 Z"/>
    </svg>

    <div class="brand">
      <span class="brand__dot"></span>
      <span class="brand__name">
        <span class="brand__main">BRIARVALE</span>
        <span class="brand__sub">AUTO LINK</span>
      </span>
    </div>

    <ul class="contact">
      <li>
        <svg viewBox="0 0 10 10" aria-hidden="true"><path d="M1,3 C1,1 9,1 9,3 L7,4 L6,3 L4,3 L3,4 Z M2,5 L8,5 L9,9 L1,9 Z"/></svg>
        555-214-7730
      </li>
      <li>
        <svg viewBox="0 0 10 10" aria-hidden="true"><circle cx="5" cy="5" r="4.5"/></svg>
        www.BriarvaleAutoLink.example
      </li>
      <li>
        <svg viewBox="0 0 10 10" aria-hidden="true"><path d="M0,2 L10,2 L5,6 Z M0,3.5 L5,7.5 L10,3.5 L10,8.5 L0,8.5 Z"/></svg>
        Drew@BriarvaleAutoLink.example
      </li>
    </ul>

    <div class="person">
      <div class="person__name">DREW</div>
      <div class="person__role">Managing Director</div>
    </div>
  </section>
</main>
</body>
</html>
```